Tarrow Structural Approval Standards Private Assessors

Professional Construction Consultancy Company Business Card - must keep logo colours see images below - examples have been added from my last competition - please see them as examples only!

Target Market(s)

Home Builders

Industry/Entity Type

Construction

Contact Information for Business Card

See "must haves"

Font styles to use
Sans Serif

Colors
ffffff
add136
000000

Requirements
Must have
• Daniel Moravi
• Director
• Phone: 0431 587 219
• Address: 7 Tarrunga Rd,
• Hallworth Vale, SA, 5091
• Email: tarrowassessors@mailbox-example.com
• Website: www.tarrowassessors-example.com.au
• Facebook: Tarrow Structural Approval Standards
Nice to have
• Side 1: full logo
• Side 2: company details
Should not have
• hard to read
• must be clear and professional

```html
<!DOCTYPE html>
<html lang="en">
<head>
<meta charset="utf-8">
<title>Tarrow Structural Approval Standards – Business Card</title>
<link rel="stylesheet" href="https://fonts.googleapis.com/css2?family=Montserrat:wght@700&family=Open+Sans:wght@400;600&display=swap">
<style>
  :root {
    --green: #add136;
    --black: #000000;
    --ink: #1d1d1b;
    --white: #ffffff;
    --stage: #e6e7e3;
  }
  * { box-sizing: border-box; margin: 0; padding: 0; }
  html, body { width: 1200px; height: 810px; overflow: hidden; }
  body { background: var(--stage); position: relative; font-family: "Open Sans", Arial, sans-serif; }

  .card {
    position: absolute;
    width: 540px;
    height: 309px;
    overflow: hidden;
    box-shadow: 0 6px 18px rgba(0,0,0,.18);
  }
  .card--front { left: 40px; top: 250px; background: var(--green); }
  .card--back  { left: 620px; top: 250px; background: var(--white); }

  .brand {
    font-family: "Montserrat", Arial, sans-serif;
    font-weight: 700;
    color: var(--ink);
    display: flex;
    align-items: center;
    gap: 12px;
    white-space: nowrap;
  }
  .brand__mark { width: 30px; height: 30px; background: var(--ink); flex: none; }
  .brand__name { line-height: 1.2; letter-spacing: .5px; text-transform: uppercase; }

  .card--front .brand { position: absolute; left: 0; right: 0; top: 92px; justify-content: center; }
  .card--front .brand__name { font-size: 18px; }
  .front__web {
    position: absolute; left: 0; right: 0; bottom: 40px;
    text-align: center; font-size: 12px; color: var(--ink);
  }

  .card--back .brand { position: absolute; left: 40px; top: 78px; }
  .card--back .brand__name { font-size: 14px; }

  .tab { position: absolute; right: 0; top: 28px; width: 12px; height: 30px; background: var(--green); border-radius: 6px 0 0 6px; }

  .person { position: absolute; right: 30px; top: 38px; text-align: right; }
  .person__name { font-weight: 600; font-size: 15px; color: var(--green); }
  .person__role { font-size: 11px; color: var(--ink); }

  .swoosh { position: absolute; inset: 0; width: 540px; height: 309px; }

  .contacts { position: absolute; left: 40px; top: 160px; list-style: none; font-size: 11px; color: var(--ink); }
  .contacts li { display: flex; align-items: center; gap: 7px; margin-bottom: 4px; line-height: 1.3; }
  .contacts li.gap { margin-bottom: 10px; }
  .icon { width: 16px; height: 16px; flex: none; }

  .back__web {
    position: absolute; left: 0; right: 0; bottom: 10px; text-align: center;
    font-size: 13px; color: var(--ink);
  }
</style>
</head>
<body>

  <section class="card card--front" aria-label="Card front">
    <div class="brand">
      <span class="brand__mark"></span>
      <span class="brand__name">Tarrow Structural<br>Approval Standards<br>Private Assessors</span>
    </div>
    <p class="front__web">www.tarrowassessors-example.com.au</p>
  </section>

  <section class="card card--back" aria-label="Card back">
    <svg class="swoosh" viewBox="0 0 540 309" aria-hidden="true">
      <path d="M0,309 L0,302 C170,285 400,255 540,160 L540,309 Z" fill="var(--green)"/>
      <path d="M300,250 C400,236 485,200 540,128 L540,150 C485,215 400,245 300,250 Z" fill="var(--ink)"/>
    </svg>

    <span class="tab"></span>

    <div class="person">
      <p class="person__name">Daniel Moravi</p>
      <p class="person__role">Director</p>
    </div>

    <div class="brand">
      <span class="brand__name">Tarrow Structural Approval Standards<br>Private Assessors</span>
    </div>

    <ul class="contacts">
      <li class="gap">
        <svg class="icon" viewBox="0 0 16 16" aria-hidden="true"><circle cx="8" cy="8" r="8" fill="var(--green)"/><path d="M8 3.5a3 3 0 0 0-3 3c0 2.2 3 5.5 3 5.5s3-3.3 3-5.5a3 3 0 0 0-3-3z" fill="var(--white)"/><circle cx="8" cy="6.5" r="1.1" fill="var(--green)"/></svg>
        <span>7 Tarrunga Rd,<br>Hallworth Vale, SA, 5091</span>
      </li>
      <li>
        <svg class="icon" viewBox="0 0 16 16" aria-hidden="true"><circle cx="8" cy="8" r="8" fill="var(--green)"/><path d="M5.2 4.2l1.5-.3.9 2.1-1 .8a5.5 5.5 0 0 0 2.6 2.6l.8-1 2.1.9-.3 1.5c-3.6.4-7-3-6.6-6.6z" fill="var(--white)"/></svg>
        <span>0431 587 219</span>
      </li>
      <li>
        <svg class="icon" viewBox="0 0 16 16" aria-hidden="true"><circle cx="8" cy="8" r="8" fill="var(--green)"/><rect x="4" y="5.2" width="8" height="5.6" fill="var(--white)"/><path d="M4 5.4l4 3 4-3" fill="none" stroke="var(--green)" stroke-width=".9"/></svg>
        <span>tarrowassessors@mailbox-example.com</span>
      </li>
      <li>
        <svg class="icon" viewBox="0 0 16 16" aria-hidden="true"><circle cx="8" cy="8" r="8" fill="var(--green)"/></svg>
        <span>Tarrow Structural Approval Standards</span>
      </li>
    </ul>

    <p class="back__web">www.tarrowassessors-example.com.au</p>
  </section>

</body>
</html>
```